brightmolar flyer on both sides

Need to design a flyer for brightmolar practice
emphasis on quality patient care

incorporate our partners QMP, RTWA and VLOKE.
ALL other health funds accepted with TORVEX

special offer: bring your family in for no gap dental clean,exam,x ray and fluoride treatments

second page-cosmetic dentistry
MODEL- WITH NICE TEETH

Aesthetic assessment- no charge for consult only with printed treatment plan at the end of consult. 20% off makeovers

sample implant flyer we used previously attached

Target Market(s)

families and patients looking for cosmetic dentistry

Industry/Entity Type

Health

Requirements
Must have
• our practice logo, phone number,web address, address
Nice to have
• eye catching, less clinical

```html
<!DOCTYPE html>
<html lang="en">
<head>
<meta charset="utf-8">
<title>Brightmolar Flyer – Both Sides</title>
<link rel="stylesheet" href="https://fonts.googleapis.com/css2?family=Jost:wght@300;400;500;600;700&family=Open+Sans:wght@400;600;700&family=Dancing+Script:wght@500&display=swap">
<style>
  :root {
    --page-bg: #ececec;
    --paper: #ffffff;
    --brand-blue: #1f6fd1;
    --brand-deep: #1458b0;
    --sky: #3aa8e0;
    --script-cyan: #2bc4d8;
    --ink: #2b2b2b;
    --ink-soft: #555555;
    --peach: #fcd7b5;
    --pink: #e0488f;
    --rule: #bdbdbd;
  }
  * { box-sizing: border-box; margin: 0; padding: 0; }
  html, body { width: 1200px; height: 852px; overflow: hidden; }
  body { background: var(--page-bg); font-family: "Open Sans", Arial, sans-serif; position: relative; }

  .flyer {
    position: absolute; width: 560px; height: 396px; background: var(--paper);
    overflow: hidden; box-shadow: 0 4px 14px rgba(0,0,0,.18);
  }
  .flyer--cosmetic { left: 30px; top: 70px; }
  .flyer--family { left: 610px; top: 386px; }

  .brand { position: absolute; display: flex; align-items: center; gap: 6px;
    font-family: "Jost", sans-serif; font-weight: 600; color: var(--brand-blue); letter-spacing: .5px; }
  .brand__dot { width: 10px; height: 10px; border-radius: 50%; background: var(--sky); }

  /* Cosmetic side */
  .cosmetic__photo { position: absolute; left: 0; top: 0; width: 240px; height: 396px;
    background: linear-gradient(135deg, #f1e2b8 0%, #e9c9a8 35%, #d9b39a 55%, #8e8e8e 80%, #6f6f6f 100%); }
  .cosmetic__brand { left: 258px; top: 44px; font-size: 12px; }
  .cosmetic__divider { position: absolute; left: 362px; top: 26px; width: 1px; height: 66px; background: var(--sky); }
  .cosmetic__dentist { position: absolute; left: 372px; top: 24px; font-family: "Jost", sans-serif; }
  .dentist__name { font-size: 16px; font-weight: 600; color: var(--brand-blue); }
  .dentist__name small { font-family: "Open Sans", sans-serif; font-size: 7px; font-weight: 400; color: var(--ink-soft); margin-left: 4px; }
  .dentist__practice { font-size: 10px; color: var(--sky); line-height: 12px; margin-top: 2px; }
  .cosmetic__address { position: absolute; left: 372px; top: 74px; font-size: 10px; color: var(--ink); }
  .cosmetic__band { position: absolute; right: 0; top: 108px; width: 220px; height: 96px; }
  .cosmetic__band-title { position: absolute; right: 14px; top: 118px; width: 150px; text-align: right;
    font-family: "Jost", sans-serif; font-weight: 700; font-size: 19px; line-height: 20px; color: #fff; }
  .cosmetic__band-note { position: absolute; right: 14px; top: 162px; width: 150px; text-align: right;
    font-size: 8px; line-height: 10px; color: #fff; }
  .cosmetic__tagline { position: absolute; left: 258px; top: 114px; font-family: "Dancing Script", cursive;
    font-size: 22px; color: var(--script-cyan); }
  .discount { position: absolute; left: 264px; top: 160px; width: 96px; height: 96px; border-radius: 50%;
    background: var(--brand-blue); border: 4px solid #fff; box-shadow: 0 0 0 2px var(--brand-blue);
    color: #fff; font-family: "Jost", sans-serif; text-align: center; padding-top: 20px; }
  .discount__value { font-size: 34px; font-weight: 700; line-height: 34px; }
  .discount__label { font-size: 10px; }
  .services { position: absolute; left: 300px; top: 276px; list-style: none; font-size: 9px; line-height: 13px; color: var(--ink); }
  .services .is-accent { color: var(--brand-blue); }

  /* Family side */
  .family__brand { left: 30px; top: 20px; font-size: 13px; }
  .family__rule { position: absolute; left: 30px; top: 48px; width: 260px; height: 1px;
    background: linear-gradient(90deg, var(--rule), #777); }
  .family__heading { position: absolute; left: 30px; top: 58px; width: 260px; font-family: "Jost", sans-serif; font-weight: 300; }
  .family__lead { font-size: 20px; color: var(--ink); line-height: 24px; }
  .family__services { font-size: 20px; color: var(--brand-blue); line-height: 23px; }
  .offer { position: absolute; width: 108px; height: 96px; background: var(--peach); border-radius: 8px;
    text-align: center; font-family: "Jost", sans-serif; color: var(--ink); padding-top: 34px; }
  .offer--adult { left: 46px; top: 220px; }
  .offer--kids { left: 170px; top: 240px; }
  .offer__ribbon { position: absolute; left: -8px; top: 4px; width: 124px; height: 24px; background: var(--brand-blue);
    color: #fff; font-size: 13px; line-height: 24px; }
  .offer__price { font-size: 28px; font-weight: 600; color: var(--brand-deep); line-height: 30px; }
  .offer__who { font-size: 13px; }
  .family__photo { position: absolute; left: 282px; top: 70px; width: 278px; height: 300px;
    background: linear-gradient(160deg, #efe7e0 0%, #d9b8a0 40%, #f3f3f3 65%, #9fcf6e 100%); }
  .partners { position: absolute; left: 26px; top: 338px; }
  .partners__label { font-size: 6px; color: var(--brand-blue); }
  .partners__list { display: flex; gap: 10px; align-items: center; margin-top: 4px; list-style: none;
    font-family: "Open Sans", sans-serif; font-weight: 700; font-size: 9px; color: var(--brand-blue); }
  .partners__badge { width: 22px; height: 12px; border-radius: 3px; background: var(--pink); }
  .funds { position: absolute; left: 196px; top: 336px; font-size: 6px; color: var(--ink-soft); width: 90px; }
  .funds__name { display: flex; align-items: center; gap: 4px; margin-top: 3px; font-weight: 700; font-size: 9px; color: var(--ink); }
  .funds__name i { width: 7px; height: 7px; border-radius: 50%; background: var(--ink); }
  .family__footer { position: absolute; left: 0; bottom: 0; width: 560px; height: 8px; background: var(--brand-blue); }
</style>
</head>
<body>

<section class="flyer flyer--cosmetic" aria-label="Cosmetic dentistry side">
  <div class="cosmetic__photo" role="img" aria-label="Photo of a smiling blonde woman with bright teeth"></div>
  <div class="brand cosmetic__brand"><span class="brand__dot"></span>BRIGHTMOLAR</div>
  <div class="cosmetic__divider"></div>
  <div class="cosmetic__dentist">
    <p class="dentist__name">Dr. Marcus Vell<small>B.D.S hons (London)</small></p>
    <p class="dentist__practice">Now practicing at<br>Brightmolar in Kelvale</p>
  </div>
  <p class="cosmetic__address">422 Linden Road Kelvale VIC 3190</p>
  <svg class="cosmetic__band" viewBox="0 0 220 96" aria-hidden="true">
    <polygon points="70,0 220,0 220,96 0,96" fill="#1f6fd1"/>
  </svg>
  <p class="cosmetic__band-title">Aesthetic Assessment-</p>
  <p class="cosmetic__band-note">No charge consult with printed treatment plan</p>
  <p class="cosmetic__tagline">Putting patients first</p>
  <div class="discount">
    <p class="discount__value">20%</p>
    <p class="discount__label">off makeovers</p>
  </div>
  <ul class="services">
    <li>Smile Makeovers</li>
    <li class="is-accent">Facial Aesthetics</li>
    <li>General Dentistry</li>
  </ul>
</section>

<section class="flyer flyer--family" aria-label="Family offer side">
  <div class="brand family__brand"><span class="brand__dot"></span>BRIGHTMOLAR</div>
  <div class="family__rule"></div>
  <div class="family__heading">
    <p class="family__lead">Bring Your Family in</p>
    <p class="family__services">For Examination,<br>Clean Fluoride and<br>All Necessary Dental<br>X-Rays for</p>
  </div>
  <div class="offer offer--adult">
    <p class="offer__ribbon">Special Offer</p>
    <p class="offer__price">$200</p>
    <p class="offer__who">for adult</p>
  </div>
  <div class="offer offer--kids">
    <p class="offer__ribbon">Special Offer</p>
    <p class="offer__price">$50</p>
    <p class="offer__who">for kids</p>
  </div>
  <div class="family__photo" role="img" aria-label="Photo of a happy, laughing family of several generations"></div>
  <div class="partners">
    <p class="partners__label">Incorporate our Partners :</p>
    <ul class="partners__list">
      <li>RTWA</li>
      <li>QMP</li>
      <li>VLOKE</li>
      <li class="partners__badge" aria-label="Partner badge"></li>
    </ul>
  </div>
  <div class="funds">
    <p>ALL other Health Funds Accepted with TORVEX</p>
    <p class="funds__name"><i></i>TORVEX</p>
  </div>
  <div class="family__footer"></div>
</section>

</body>
</html>
```